Business Card, Stationary with Shark Logo for Personal Injury Lawyer

I need business cards and stationery with a shark logo for my Personal Injury Law Practice. Has to have this written on it:
Martin K. Hollis
Injury Lawyer
The Corvell Building
718 Tandy Street
Providence, Rhode Island 02908
401-627-4193
Martinhollis.com

Contact Information for Business Card

Martin K. Hollis, Injury Lawyer, address, 401-627-4193, martinhollis.com

```html
<!DOCTYPE html>
<html lang="en">
<head>
<meta charset="utf-8">
<title>Martin K. Hollis – Business Card</title>
<link rel="stylesheet" href="https://fonts.googleapis.com/css2?family=Roboto+Condensed:wght@700&family=Open+Sans:wght@400&display=swap">
<style>
  :root {
    --page-bg: #e6e6e6;
    --card-white: #f6f6f7;
    --navy: #27245e;
    --navy-deep: #201d52;
    --navy-back: #2b2866;
    --navy-mark: #3b3780;
    --grey-text: #6a6a72;
    --ink: #3a3a44;
  }
  * { margin: 0; padding: 0; box-sizing: border-box; }
  html, body {
    width: 1200px; height: 1200px; overflow: hidden;
    background: var(--page-bg);
  }
  .canvas { position: relative; width: 1200px; height: 1200px; }
  .card {
    position: absolute; left: 262px; width: 686px; height: 391px;
    border-radius: 18px; overflow: hidden;
  }
  .card-front { top: 165px; background: var(--card-white); }
  .card-back {
    top: 653px;
    background: linear-gradient(180deg, var(--navy-back) 0%, var(--navy-deep) 100%);
    display: flex; align-items: center; justify-content: center;
  }
  .brand-name {
    font-family: "Roboto Condensed", sans-serif; font-weight: 700;
    text-transform: uppercase; line-height: 1;
  }
  .front-brand {
    position: absolute; top: 62px; right: 44px;
    font-size: 38px; color: var(--navy); letter-spacing: 0.5px;
  }
  .holder { position: absolute; left: 51px; top: 168px; }
  .holder-name { font-size: 27px; color: var(--navy); }
  .holder-title {
    font-family: "Open Sans", sans-serif; font-size: 16px;
    color: var(--grey-text); margin-top: 6px;
  }
  .contact-list { list-style: none; margin-top: 14px; }
  .contact-item {
    display: flex; align-items: flex-start; gap: 10px;
    font-family: "Open Sans", sans-serif; font-size: 14.5px;
    color: var(--ink); line-height: 21px;
  }
  .contact-item svg { width: 14px; height: 14px; flex: none; margin-top: 3.5px; }
  .mark-area {
    position: absolute; right: 70px; bottom: 10px;
    width: 150px; height: 150px; background: var(--navy);
  }
  .bottom-band {
    position: absolute; left: 0; right: 0; bottom: 0; height: 10px;
    background: var(--navy);
  }
  .back-brand {
    font-size: 64px; color: var(--navy-mark); letter-spacing: 1px;
  }
</style>
</head>
<body>
<main class="canvas">
  <section class="card card-front">
    <div class="brand-name front-brand">Martin K. Hollis</div>
    <div class="holder">
      <h1 class="brand-name holder-name">Martin K. Hollis</h1>
      <p class="holder-title">Injury Lawyer</p>
      <ul class="contact-list">
        <li class="contact-item">
          <svg viewBox="0 0 16 16" aria-hidden="true"><path d="M8 1a5 5 0 0 0-5 5c0 3.5 5 9 5 9s5-5.5 5-9a5 5 0 0 0-5-5z" fill="#27245e"/><circle cx="8" cy="6" r="1.8" fill="#f6f6f7"/></svg>
          <span>The Corvell Building, 718 Tandy Street<br>Providence, Rhode Island 02908</span>
        </li>
        <li class="contact-item">
          <svg viewBox="0 0 16 16" aria-hidden="true"><path d="M4 1.5 6.5 4 5 6c.8 1.8 2.2 3.2 4 4l2-1.5 2.5 2.5-1.5 2.5C7 13 3 9 1.5 3z" fill="#27245e"/></svg>
          401-627-4193
        </li>
        <li class="contact-item">
          <svg viewBox="0 0 16 16" aria-hidden="true"><rect x="1" y="3" width="14" height="10" fill="#27245e"/><path d="M1.5 3.5 8 9l6.5-5.5" fill="none" stroke="#f6f6f7" stroke-width="1.3"/></svg>
          Martin@martinhollis.com
        </li>
        <li class="contact-item">
          <svg viewBox="0 0 16 16" aria-hidden="true"><circle cx="8" cy="8" r="7" fill="#27245e"/><path d="M5 4.5c1.5.5 2 1.5 1.5 2.5S4.5 8.5 5 10s2 1.5 2 3M10 3.5c-.5 1.5.5 2.5 2 2.5M11 9c-1 .5-1 2 0 3" fill="none" stroke="#f6f6f7" stroke-width="1.2"/></svg>
          Martinhollis.com
        </li>
      </ul>
    </div>
    <div class="mark-area" role="img" aria-label="Space for the practice's shark logo mark"></div>
    <div class="bottom-band"></div>
  </section>

  <section class="card card-back">
    <div class="brand-name back-brand">Martin K. Hollis</div>
  </section>
</main>
</body>
</html>
```